Podcast Cover Art for Fast Growing Show (Ill include a gracious tip!)

This artwork is for "The Steadfast Fellow Show." The podcast is for men, and it's all about self-improvement, confidence, success, money, women and masculinity. It's for the guy who wants to improve himself. I'd like for my picture to be included — in black and white — and I want the text to read: "The Steadfast Fellow Show" and somewhere in there it'll say: "with Dale Prowen." I'm open to color schemes. The podcast is a little edgy so I'd like for that to be represented in the design. Thank you! (((Here's the podcast page if you wanna check it out: http://steadfastfellowshow.castorbit.net/)))

Target Market(s)

Men who want to attract women and improve their lives!

Font styles to use
Serif

Colors

Designer to choose colors to be used in the design.

Requirements
Must have
• My image in it (in black and white) and the two titles: "The Steadfast Fellow Show" and "with Dale Prowen"
Nice to have
• My logo in it somehow (which is the arrow looking logo attached below). I've also found that my image looks best in black and white and with a circular type cut out (although I'm open to different design ideas). I've attached my logo with a circular cut out below so you can see what I'm talking about.
Should not have
• Flowers. Teddy bears. ice cream.

```html
<!DOCTYPE html>
<html lang="en">
<head>
<meta charset="utf-8">
<title>The Steadfast Fellow Show – Podcast Cover</title>
<link rel="stylesheet" href="https://fonts.googleapis.com/css2?family=DM+Serif+Display:ital@0;1&family=Montserrat:wght@400;800&display=swap">
<style>
  :root {
    --page-bg: #f1f1f1;
    --cover-black: #0b0b0b;
    --cover-charcoal: #1c1c1c;
    --photo-light: #8c8c8c;
    --photo-mid: #4a4a4a;
    --photo-dark: #161616;
    --title-white: #ffffff;
    --accent-red: #e41b17;
  }
  * { margin: 0; padding: 0; box-sizing: border-box; }
  html, body {
    width: 1200px;
    height: 869px;
    overflow: hidden;
    background: var(--page-bg);
  }
  .canvas {
    position: relative;
    width: 1200px;
    height: 869px;
    display: flex;
    align-items: center;
    justify-content: center;
  }
  .cover {
    position: relative;
    width: 780px;
    height: 780px;
    overflow: hidden;
    background: radial-gradient(ellipse at 30% 20%, var(--cover-charcoal) 0%, var(--cover-black) 70%);
  }
  .host-portrait {
    position: absolute;
    top: 25px;
    right: 0;
    width: 470px;
    height: 755px;
    border-radius: 48% 48% 0 0 / 30% 30% 0 0;
    background:
      radial-gradient(ellipse at 50% 32%, var(--photo-light) 0%, var(--photo-mid) 34%, transparent 62%),
      linear-gradient(180deg, var(--photo-dark) 0%, var(--photo-mid) 55%, var(--photo-dark) 100%);
    opacity: 0.9;
  }
  .show-title {
    position: absolute;
    left: 44px;
    top: 318px;
    font-family: 'DM Serif Display', Georgia, serif;
    font-weight: 400;
    color: var(--title-white);
    text-shadow: 0 2px 12px rgba(0, 0, 0, 0.6);
  }
  .show-title .line { display: block; }
  .show-title .line-the {
    font-style: italic;
    font-size: 40px;
    line-height: 1;
    margin-bottom: 6px;
  }
  .show-title .line-main {
    font-size: 82px;
    line-height: 0.98;
  }
  .title-rule {
    position: absolute;
    left: 46px;
    top: 560px;
    width: 120px;
    height: 5px;
    background: var(--accent-red);
  }
  .host-credit {
    position: absolute;
    left: 42px;
    top: 628px;
    font-family: 'Montserrat', 'Helvetica Neue', sans-serif;
    color: var(--title-white);
  }
  .host-credit .with {
    display: block;
    font-weight: 400;
    font-size: 24px;
    margin-left: 3px;
    letter-spacing: 0.5px;
  }
  .host-credit .host-name {
    display: block;
    font-weight: 800;
    font-size: 40px;
    line-height: 1.1;
  }
</style>
</head>
<body>
  <main class="canvas">
    <section class="cover">
      <div class="host-portrait" role="img" aria-label="Black and white portrait of the host, Dale Prowen, with fingertips pressed together beneath his chin"></div>
      <h1 class="show-title">
        <span class="line line-the">The</span>
        <span class="line line-main">Steadfast</span>
        <span class="line line-main">Fellow Show</span>
      </h1>
      <div class="title-rule"></div>
      <p class="host-credit">
        <span class="with">With</span>
        <span class="host-name">Dale Prowen</span>
      </p>
    </section>
  </main>
</body>
</html>
```